Seven Quiet Rooms Poster

Seven Quiet Rooms is reaching out to designers, creatives and fans alike to help create an exciting new poster for the film as part of our Fundvaro campaign.

Seven Quiet Rooms is a multi-protagonist, multicultural, humanist drama inspired by the 2008 Mumbai terrorist attacks. Centering on a group of international tourists trapped in their hotel by Islamic fundamentalists, the film aims to explore the key issues facing our society, concerning atheism, religion, religious extremism and humanism.

The film’s poster will be a critical part of a film’s publicity and marketing portfolio and an important resource for the film to take into our festival campaign and distribution talks. We’re looking for a highly polished design that accurately represents the film and matches the standard of the finished film.

We will be uploading some of the best entries to our Chatterbox page for fans to vote on. If you do not wish for your design to appear on the page, please contact us.

You can find our teaser trailer on the Fundvaro link below. We’ve also provided some reference images (found here: http://lnk.example-short.net/Rk4WpZ) and also stills from the film to provide inspiration (found here: http://lnk.example-short.net/Tm8QvB) - how or if you use them is up to you.

Good luck and get designing!

http://www.fundvaro-example.com/projects/seven-quiet-rooms

Please note: Amber Tide Pictures reserves the right to select all promotional material for theatrical release.

Requirements
Must have
• Size: 27" x 40"
Should not have
• Please do not include the credit block on your designs.

```html
<!DOCTYPE html>
<html lang="en">
<head>
<meta charset="utf-8">
<title>Seven Quiet Rooms — Poster</title>
<link rel="stylesheet" href="https://fonts.googleapis.com/css2?family=Open+Sans:wght@400;800&display=swap">
<style>
  :root {
    --ink-white: #ffffff;
    --soft-white: rgba(255, 255, 255, 0.9);
    --shadow-brown: #241b1a;
    --skin-light: #8a6a5c;
    --skin-mid: #6b5047;
    --skin-deep: #3e2d2a;
    --hair-dark: #1f1718;
    --haze-grey: #8e8d99;
    --haze-light: #cfd0d8;
    --scarf-green: #2c3a2c;
    --lip-rose: #6a4040;
  }
  html, body {
    margin: 0;
    padding: 0;
    overflow: hidden;
    background: var(--shadow-brown);
  }
  .poster {
    position: relative;
    width: 811px;
    height: 1200px;
    overflow: hidden;
    font-family: "Open Sans", Arial, sans-serif;
    color: var(--ink-white);
  }
  .poster-photo {
    position: absolute;
    inset: 0;
    background:
      /* soft light haze behind the hair on the right */
      radial-gradient(ellipse 22% 20% at 86% 40%, var(--haze-light) 0%, rgba(207,208,216,0) 100%),
      radial-gradient(ellipse 30% 30% at 80% 26%, rgba(142,141,153,0.95) 0%, rgba(142,141,153,0) 100%),
      /* dark hair falling down the right edge */
      radial-gradient(ellipse 24% 30% at 92% 70%, var(--hair-dark) 0%, rgba(31,23,24,0) 100%),
      radial-gradient(ellipse 26% 14% at 72% 4%, var(--hair-dark) 0%, rgba(31,23,24,0) 100%),
      /* scarf tone near the lower centre */
      radial-gradient(ellipse 12% 10% at 54% 73%, var(--scarf-green) 0%, rgba(44,58,44,0) 100%),
      /* warm skin tones filling the left side */
      radial-gradient(ellipse 18% 10% at 8% 60%, var(--lip-rose) 0%, rgba(106,64,64,0) 100%),
      radial-gradient(ellipse 34% 30% at 28% 36%, var(--skin-light) 0%, rgba(138,106,92,0) 100%),
      radial-gradient(ellipse 46% 46% at 30% 40%, var(--skin-mid) 0%, rgba(107,80,71,0) 100%),
      radial-gradient(ellipse 30% 18% at 60% 48%, rgba(95,72,66,0.9) 0%, rgba(95,72,66,0) 100%),
      linear-gradient(180deg, #2b2022 0%, var(--skin-deep) 20%, #3a2c2b 55%, var(--shadow-brown) 100%);
  }
  .poster-photo::after {
    content: "";
    position: absolute;
    inset: 0;
    background: linear-gradient(180deg, rgba(0,0,0,0.15) 0%, rgba(0,0,0,0) 12%, rgba(0,0,0,0) 50%, rgba(20,14,14,0.5) 100%);
  }
  .title-block {
    position: absolute;
    left: 0;
    right: 0;
    top: 668px;
    text-align: center;
  }
  .film-title {
    margin: 0;
    font-weight: 800;
    font-size: 68px;
    line-height: 1;
    letter-spacing: 3px;
    text-transform: uppercase;
    white-space: nowrap;
  }
  .film-subtitle {
    margin: 14px 0 0;
    font-weight: 400;
    font-size: 25px;
    line-height: 34px;
    color: var(--soft-white);
  }
  .quote-block {
    position: absolute;
    left: 0;
    right: 0;
    top: 962px;
    text-align: center;
  }
  .quote-text {
    margin: 0 auto;
    width: 545px;
    font-size: 22px;
    line-height: 44px;
    hyphens: auto;
    -webkit-hyphens: auto;
    color: var(--soft-white);
  }
  .quote-author {
    margin: 26px 0 0;
    font-size: 20px;
    line-height: 28px;
    color: var(--soft-white);
  }
</style>
</head>
<body>
  <main class="poster">
    <div class="poster-photo" role="img" aria-label="Close-up photograph of a frightened young girl in dim light, filling the upper poster, her dark hair blurred against a hazy grey background and a green scarf at her neck"></div>

    <header class="title-block">
      <h1 class="film-title">Seven Quiet Rooms</h1>
      <p class="film-subtitle">2008 Mumbai terrorist attacks</p>
    </header>

    <section class="quote-block">
      <p class="quote-text">“If our children can die for the sake of our be&shy;liefs, maybe it’s time our beliefs started dying for the sake of our children.”</p>
      <p class="quote-author">M. Ashcombe</p>
    </section>
  </main>
</body>
</html>
```